Business card design for new eCommerce site focusing on integrity and strong businsess tactics

We need a business card that will stand out and be memorable. Something with color that matches our company logo colors. Think high end version of Dealvine. There are 2 logos provided. The parent company is called Bright Harbor Ventures and we are presenting a new and very exciting eCommerce site called KeenTraders.example.

Target Market(s)

Our target markets are in the Activities, Food and Beverage, Health and Beauty

Industry/Entity Type

Marketing

Contact Information for Business Card

We have 4 members that need cards...I will provide all info to the winner of the design contest
Business Address is
48730 West 61st Avenue, Suite C204
Phoenix AZ 85917

Font styles to use
Serif
Sans Serif

Colors

Designer to choose colors to be used in the design.

Requirements
Must have
• The card must be memorable...should be unique in design but must exude integrity and be playful .
• I have provided several colors or our parent company...please feel free to use which ever
Nice to have
• I will leave this up to you. Feel free to use other images of your choosing that wraps around our client.....Activities, Dining, Health, Beauty
Should not have
• just dont be boring

```html
<!DOCTYPE html>
<html lang="en">
<head>
<meta charset="utf-8">
<title>Bright Harbor Ventures – Business Card</title>
<link rel="stylesheet" href="https://fonts.googleapis.com/css2?family=Open+Sans:wght@400;600;700&display=swap">
<style>
  :root {
    --stage: #2a2a2c;
    --card-white: #f7f7f8;
    --card-shade: #e6e7e9;
    --navy: #121c4a;
    --ink-navy: #14204f;
    --brand-green: #6aac2a;
    --brand-blue: #2b6cb0;
    --accent-gold: #f2b51c;
    --band-text: #e9ecf5;
    --divider: #8c93ad;
  }
  * { box-sizing: border-box; margin: 0; padding: 0; }
  html, body { width: 1200px; height: 904px; overflow: hidden; }
  body {
    background: var(--stage);
    font-family: "Open Sans", Arial, sans-serif;
    position: relative;
  }
  .card {
    position: absolute;
    width: 560px;
    height: 320px;
    background: linear-gradient(135deg, var(--card-white) 0%, #ffffff 45%, var(--card-shade) 100%);
    box-shadow: 0 14px 30px rgba(0,0,0,0.45);
    overflow: hidden;
  }
  /* Front */
  .card-front { left: 110px; top: 90px; }
  .front-brand {
    position: absolute;
    left: 70px; top: 138px;
    display: flex; align-items: center; gap: 12px;
  }
  .front-brand .mark {
    width: 26px; height: 26px; border-radius: 50%;
    background: var(--brand-blue);
  }
  .front-brand .name {
    font-weight: 700; font-size: 30px; color: var(--brand-green);
    letter-spacing: -0.3px;
  }
  /* Back */
  .card-back { left: 530px; top: 480px; }
  .back-brand {
    position: absolute; left: 40px; top: 34px;
    display: flex; flex-direction: column; align-items: flex-start; gap: 12px;
  }
  .back-brand .mark {
    width: 86px; height: 86px; border-radius: 50%;
    background: var(--navy);
    box-shadow: 0 0 0 3px #fff, 0 0 0 4px var(--navy);
    margin-left: 8px;
  }
  .back-brand .name {
    font-weight: 700; font-size: 23px; color: var(--ink-navy);
  }
  .holder {
    position: absolute; right: 34px; top: 92px; text-align: right;
  }
  .holder .person { font-weight: 700; font-size: 18px; color: var(--ink-navy); }
  .holder .role { font-size: 12px; color: #222; }
  .info-band {
    position: absolute; left: 0; right: 0; bottom: 0; height: 128px;
    background: var(--navy);
    display: flex; align-items: center; padding: 0 34px;
    color: var(--band-text); font-size: 13.5px; line-height: 1.55;
  }
  .address { width: 232px; }
  .band-divider { width: 1px; height: 62px; background: var(--divider); margin: 0 22px; }
  .contacts { list-style: none; }
  .contacts li { display: flex; align-items: center; gap: 9px; }
  .contacts svg { width: 13px; height: 13px; flex: none; }
</style>
</head>
<body>

<section class="card card-front" aria-label="Card front">
  <div class="front-brand">
    <span class="mark"></span>
    <span class="name">KeenTraders.example</span>
  </div>
</section>

<section class="card card-back" aria-label="Card back">
  <div class="back-brand">
    <span class="mark"></span>
    <span class="name">Bright Harbor Ventures</span>
  </div>
  <div class="holder">
    <p class="person">Alan Mercer</p>
    <p class="role">Manager</p>
  </div>
  <div class="info-band">
    <address class="address" style="font-style:normal">
      48730 West 61st Avenue<br>Suite C204<br>Phoenix AZ 85917
    </address>
    <span class="band-divider"></span>
    <ul class="contacts">
      <li>
        <svg viewBox="0 0 16 16"><path fill="var(--accent-gold)" d="M3.6 1.5l2.3 2.6-1.3 1.8c.9 2 2.5 3.6 4.5 4.5l1.8-1.3 2.6 2.3-1.4 2.2C6.6 15.3.7 9.4.9 3.1z"/></svg>
        +1 555 010 0148
      </li>
      <li>
        <svg viewBox="0 0 16 16"><rect x="1" y="3" width="14" height="10" rx="1.5" fill="var(--accent-gold)"/><path d="M1.5 4l6.5 5 6.5-5" stroke="var(--navy)" stroke-width="1.3" fill="none"/></svg>
        info@brightharbor.example
      </li>
      <li>
        <svg viewBox="0 0 16 16"><circle cx="8" cy="8" r="7" fill="var(--accent-gold)"/><g stroke="var(--navy)" stroke-width="1" fill="none"><ellipse cx="8" cy="8" rx="3" ry="7"/><path d="M1 8h14M2.5 4.5h11M2.5 11.5h11"/></g></svg>
        www.brightharbor.example
      </li>
    </ul>
  </div>
</section>

</body>
</html>
```